Loft Dental New Patient Ad designed to catch a persons eye in a busy and cluttered newspaper

a minimalist newspaper ad to attract new patients to my office. i want an ad that is reminiscent of the Seek Unusual Quince ads of 1998 or the 1960 Autohaus "Dud" ad. I would like the words Simply Bright in the middle of a blank space with the logo above, and the website and phone number with $88 new patient special info below it. The address need not be on the ad just that it is in North Haven.
i am trying to convey a modern office that does quality work with a vivid, colorful minimalist ad that catches the eye with its style and simplicity. Comparative ads in my area are very busy, generic, and homogenous.

Target Market(s)

Educated baby boomers
Health Conscious Millennials
Health Conscious Gen X

Font styles to use
Serif
Sans Serif

Colors
2369af
0493ce
00a990
abd037
fbed22
ffc214
f78f20

Requirements
Must have
• our logo
• our website
• our phone number
• $88 exam and cleaning
Nice to have
• a one word ad with one phrase in bold in the middle of blank space
• "Simply Bright"

```html
<!DOCTYPE html>
<html lang="en">
<head>
<meta charset="utf-8">
<title>Loft Dental – Simply Bright</title>
<link rel="stylesheet" href="https://fonts.googleapis.com/css2?family=Open+Sans:ital,wght@0,400;0,600;0,700;1,600;1,800&display=swap">
<style>
  :root {
    --stage: #e6e6e6;
    --lime: #abd037;
    --sun: #fbed22;
    --teal: #00a990;
    --sky: #0493ce;
    --white: #ffffff;
  }
  * { margin: 0; padding: 0; box-sizing: border-box; }
  html, body {
    width: 1200px;
    height: 936px;
    overflow: hidden;
    background: var(--stage);
    font-family: "Open Sans", Arial, sans-serif;
  }
  .ad {
    position: absolute;
    left: 289px;
    top: 28px;
    width: 622px;
    height: 880px;
    background:
      radial-gradient(circle at 50% 153px, var(--sun) 0, rgba(251,237,34,0.55) 130px, rgba(171,208,55,0) 320px),
      var(--lime);
    box-shadow: 0 10px 30px rgba(0,0,0,0.18);
    overflow: hidden;
  }
  .brand {
    position: absolute;
    top: 136px;
    left: 0;
    width: 100%;
    text-align: center;
    font-weight: 700;
    font-size: 24px;
    color: var(--sky);
    letter-spacing: -0.3px;
  }
  .headline {
    position: absolute;
    left: 174px;
    top: 356px;
    color: var(--white);
    font-style: italic;
    line-height: 0.86;
  }
  .headline .light {
    display: block;
    font-weight: 600;
    font-size: 76px;
    letter-spacing: -3px;
  }
  .headline .bold {
    display: block;
    margin-left: 20px;
    font-weight: 800;
    font-size: 98px;
    letter-spacing: -4px;
  }
  .offer {
    position: absolute;
    left: 65px;
    top: 818px;
    height: 17px;
    line-height: 17px;
    font-weight: 700;
    font-size: 13px;
    letter-spacing: 1.6px;
    color: var(--teal);
  }
  .contact-band {
    position: absolute;
    left: 257px;
    right: 0;
    top: 818px;
    height: 17px;
    line-height: 17px;
    background: var(--teal);
    color: var(--white);
    font-size: 10.5px;
    padding-left: 24px;
    white-space: nowrap;
  }
  .contact-band .divider { margin: 0 6px; }
</style>
</head>
<body>
  <main class="ad">
    <div class="brand">Loft Dental</div>

    <h1 class="headline">
      <span class="light">Simply</span>
      <span class="bold">Bright</span>
    </h1>

    <p class="offer">$88 EXAM &amp; CLEANING</p>
    <p class="contact-band">North Haven<span class="divider">|</span>203-555-0148<span class="divider">|</span>www.loft-dental.com</p>
  </main>
</body>
</html>
```